Tarnby Website

We need a web design for our company based in Sydney. Our company does many and varied acitivities. From private investments, licencing, business consultacy, payment solutions.

Our services focus on our client’s critical opportunities. We provide a range of services including strategy, marketing, compliance, organization and technology.

We can unlock your growth and potential and deliver on core strategy. We add value and bring extensive expertise in optimizing your results.

We provide also provide the following services:

 private investments,
 licensing,
 business consultancy,
 payment solutions.

Target Market(s)

Businesses

Coding

Coded - Design and coding required

Number of Pages Required

3 page

Colors

Designer to choose colors to be used in the design.

Requirements
Must have
• Corporate look and feel. two touch points, email info@tarnby.com.au and a phone number TBA
• MUST include logos and branding from attached
Nice to have
• photos

```html
<!DOCTYPE html>
<html lang="en">
<head>
<meta charset="utf-8">
<title>Tarnby</title>
<link href="https://fonts.googleapis.com/css2?family=Poppins:wght@300;400;500;600;700&family=Open+Sans:wght@400;600&display=swap" rel="stylesheet">
<style>
:root{
  --blue:#2a78c2;
  --blue-dark:#1d5fa3;
  --grey-text:#555;
  --grey-light:#8a8a8a;
  --band:#efefef;
  --footer:#1b202b;
  --white:#fff;
  --icon-box:#8c8c8c;
}
*{margin:0;padding:0;box-sizing:border-box}
html,body{width:1200px;height:2687px;overflow:hidden;background:var(--white)}
body{position:relative;font-family:"Poppins",sans-serif;color:var(--grey-text)}
.abs{position:absolute}
/* header */
.site-header{position:absolute;top:0;left:0;width:1200px;height:93px;background:var(--white)}
.brand{position:absolute;left:107px;top:22px;font:600 46px/50px "Poppins",sans-serif;color:var(--blue)}
.main-nav{position:absolute;right:106px;top:0;display:flex;gap:0;height:93px}
.main-nav a{display:block;padding:0 16px;line-height:93px;font:400 13px/93px "Poppins",sans-serif;color:#333;text-decoration:none;position:relative}
.main-nav a.active::before{content:"";position:absolute;left:0;right:0;bottom:0;height:4px;background:var(--blue)}
/* hero */
.hero{position:absolute;top:93px;left:0;width:1200px;height:609px;background:radial-gradient(ellipse at 60% 40%,#8e8e8e 0%,#5e5e5e 55%,#3c3c3c 100%)}
.hero-dots{position:absolute;top:622px;left:552px;display:flex;gap:14px}
.hero-dots span{width:10px;height:10px;border-radius:50%;background:#fff;opacity:.85}
.hero-dots span.on{background:var(--blue)}
/* intro */
.intro-title{position:absolute;top:745px;left:0;width:1200px;text-align:center;font:300 39px/47px "Poppins",sans-serif;color:#8a8a8a}
.intro-text{position:absolute;top:852px;left:0;width:1200px;text-align:center;font:400 13.5px/25px "Poppins",sans-serif;color:#444}
.quick-title{position:absolute;top:918px;left:0;width:1200px;text-align:center;font:600 25px/34px "Poppins",sans-serif;color:#555}
.email-pill{position:absolute;top:964px;left:476px;width:248px;height:48px;border-radius:24px;background:var(--blue);color:#fff;font:400 19px/48px "Poppins",sans-serif;display:flex;align-items:center;justify-content:center;gap:14px}
.phone-line{position:absolute;top:1028px;left:0;width:1200px;text-align:center;font:700 25px/36px "Poppins",sans-serif;color:var(--blue)}
/* services */
.services-band{position:absolute;top:1080px;left:0;width:1200px;height:730px}
.section-title-light{position:absolute;top:1178px;left:0;width:1200px;text-align:center;font:600 28px/36px "Poppins",sans-serif;color:#fff}
.section-sub-light{position:absolute;top:1224px;left:0;width:1200px;text-align:center;font:400 17px/26px "Poppins",sans-serif;color:#e8f0fa}
.service{position:absolute;width:460px;color:#fff}
.service-icon{position:absolute;left:0;top:0;width:59px;height:57px;background:var(--icon-box)}
.service-name{position:absolute;left:69px;top:-2px;font:400 18px/28px "Poppins",sans-serif}
.service-text{position:absolute;left:71px;top:34px;width:355px;font:400 12px/20.5px "Open Sans",sans-serif;text-align:justify;color:#f2f6fb}
.band-dots{position:absolute;top:1676px;left:584px;display:flex;gap:8px}
.band-dots span{width:9px;height:9px;border-radius:50%;background:#fff}
/* team */
.team-title{position:absolute;top:1852px;left:0;width:1200px;text-align:center;font:600 24px/32px "Poppins",sans-serif;color:#333}
.team-arrow{position:absolute;top:1990px;width:36px;height:36px;background:var(--blue);display:flex;align-items:center;justify-content:center}
.member{position:absolute;top:1925px;width:167px;text-align:center}
.member-photo{width:167px;height:167px;border-radius:50%;background:radial-gradient(circle at 50% 40%,#cfcfcf,#9a9a9a)}
.member-name{margin-top:6px;font:600 16px/22px "Poppins",sans-serif;color:#333}
/* newsletter */
.newsletter{position:absolute;top:2167px;left:0;width:1200px;height:242px;background:var(--band)}
.newsletter h2{position:absolute;top:32px;width:1200px;text-align:center;font:400 32px/42px "Poppins",sans-serif;color:#8a8a8a}
.newsletter p{position:absolute;top:80px;left:300px;width:600px;text-align:center;font:400 12.5px/22px "Poppins",sans-serif;color:#555}
.email-field{position:absolute;top:154px;left:383px;width:362px;height:36px;border:1px solid #dcdcdc;border-radius:18px;background:#fff;font:600 12.5px/34px "Poppins",sans-serif;color:#222;padding-left:22px}
.subscribe-btn{position:absolute;top:154px;left:756px;width:125px;height:36px;border-radius:18px;background:var(--blue);color:#fff;font:600 12.5px/36px "Poppins",sans-serif;text-align:center}
/* footer */
.site-footer{position:absolute;top:2409px;left:0;width:1200px;height:278px;background:var(--footer);color:#dfe3ea}
.footer-brand{position:absolute;left:120px;top:48px;font:600 44px/52px "Poppins",sans-serif;color:var(--blue)}
.footer-about{position:absolute;left:120px;top:128px;width:235px;font:400 12.5px/20px "Poppins",sans-serif;text-align:justify}
.read-more{position:absolute;left:120px;top:206px;font:400 12.5px/20px "Poppins",sans-serif;color:var(--blue)}
.footer-head{position:absolute;top:60px;font:400 20px/28px "Poppins",sans-serif;color:#fff}
.quick-links{position:absolute;top:108px;left:392px;display:grid;grid-template-columns:100px 110px;row-gap:10px;font:400 12.5px/20px "Poppins",sans-serif}
.quick-links span::before{content:"›";color:var(--blue);font-size:18px;margin-right:14px}
.contact-row{position:absolute;left:632px;display:flex;align-items:center;gap:14px;font:400 12.5px/19px "Poppins",sans-serif}
.contact-icon{width:32px;height:32px;border-radius:50%;border:1px solid #3d4656;display:flex;align-items:center;justify-content:center;flex:none}
.social{position:absolute;left:917px;top:98px;display:flex;gap:10px}
.social span{width:33px;height:33px;border-radius:50%;border:2px solid var(--blue)}
.footer-legal{position:absolute;left:917px;top:150px;font:400 12px/22px "Poppins",sans-serif}
</style>
</head>
<body>

<header class="site-header">
  <div class="brand">Tarnby</div>
  <nav class="main-nav">
    <a class="active">HOME</a><a>ABOUT</a><a>SERVICES</a><a>OUR TEAM</a><a>TESTIMONIALS</a><a>NEWS / EVENTS</a><a>CONTACT US</a>
  </nav>
</header>

<section class="hero" role="img" aria-label="Hand holding a young plant in soil against a concrete wall chalked with business gears: profit, team, quality, management"></section>
<div class="hero-dots"><span></span><span></span><span class="on"></span><span></span></div>

<h1 class="intro-title">We add value and bring extensive expertise in<br>optimising your results.</h1>
<p class="intro-text">Lorem ipsum dolor sit amet, consectetur adipiscing elit, sed do eiusmod tempor incididunt ut labore et dolore magna aliqua.<br>Ut enim ad minim veniam, quis nostrud exercitation ullamco laboris nisi ut aliquip ex ea commodo consequat.</p>
<h2 class="quick-title">Quick contact Us</h2>
<div class="email-pill">
  <svg width="24" height="24" viewBox="0 0 24 24"><circle cx="12" cy="12" r="12" fill="#fff"/><path d="M6 9l6 4 6-4v7H6z" fill="#2a78c2"/><path d="M6 8h12l-6 4z" fill="#2a78c2"/></svg>
  info@tarnby.com.au
</div>
<div class="phone-line">Phone number 1- 800 - TARNBY</div>

<svg class="services-band" viewBox="0 0 1200 730" role="img" aria-label="Blue-tinted photo of a business handshake">
  <defs>
    <linearGradient id="bandFill" x1="0" y1="0" x2="1" y2="1">
      <stop offset="0" stop-color="#2f7cc6"/><stop offset=".5" stop-color="#4a90d0"/><stop offset="1" stop-color="#246fb8"/>
    </linearGradient>
  </defs>
  <path d="M0 62 Q600 -50 1200 62 Q600 -12 0 62Z" fill="#1d63ad"/>
  <path d="M0 102 Q600 -8 1200 102 L1200 630 Q600 740 0 630Z" fill="url(#bandFill)"/>
  <path d="M0 668 Q600 780 1200 668 Q600 738 0 668Z" fill="#1d63ad"/>
</svg>
<h2 class="section-title-light">Our Services</h2>
<p class="section-sub-light">Sed ut perspiciatis unde omnis iste natus error sit</p>

<div class="service" style="left:106px;top:1327px">
  <div class="service-icon"><svg width="59" height="57" viewBox="0 0 59 57"><circle cx="29" cy="24" r="9" fill="none" stroke="#fff" stroke-width="2"/><path d="M14 42h31M20 42v-5h19v5" fill="none" stroke="#fff" stroke-width="2"/></svg></div>
  <div class="service-name">Private investments,</div>
  <p class="service-text">Sed ut perspiciatis unde omnis iste natus error sit voluptatem accusantium doloremque laudantium, totam rem aperiam, eaque ipsa quae ab illo inventore veritatis et quasi architecto</p>
</div>
<div class="service" style="left:666px;top:1327px">
  <div class="service-icon"><svg width="59" height="57" viewBox="0 0 59 57"><rect x="14" y="17" width="31" height="23" fill="none" stroke="#fff" stroke-width="2"/><circle cx="22" cy="26" r="3" fill="#fff"/><path d="M29 24h11M29 29h11M18 34h22" stroke="#fff" stroke-width="2"/></svg></div>
  <div class="service-name">Licensing</div>
  <p class="service-text">Sed ut perspiciatis unde omnis iste natus error sit voluptatem accusantium doloremque laudantium, totam rem aperiam, eaque ipsa quae ab illo inventore veritatis et quasi architecto</p>
</div>
<div class="service" style="left:106px;top:1506px">
  <div class="service-icon"><svg width="59" height="57" viewBox="0 0 59 57"><path d="M10 26l8-6 8 4 7-4 7 2 9 4M18 32l7 6 4-1 5 2 8-8" fill="none" stroke="#fff" stroke-width="2"/></svg></div>
  <div class="service-name">Business consultancy</div>
  <p class="service-text">Sed ut perspiciatis unde omnis iste natus error sit voluptatem accusantium doloremque laudantium, totam rem aperiam, eaque ipsa quae ab illo inventore veritatis et quasi architecto</p>
</div>
<div class="service" style="left:666px;top:1506px">
  <div class="service-icon"><svg width="59" height="57" viewBox="0 0 59 57"><rect x="17" y="14" width="25" height="30" fill="none" stroke="#fff" stroke-width="2"/><path d="M22 22h15M22 28h15M22 34h9" stroke="#fff" stroke-width="2"/></svg></div>
  <div class="service-name">Payment solutions</div>
  <p class="service-text">Sed ut perspiciatis unde omnis iste natus error sit voluptatem accusantium doloremque laudantium, totam rem aperiam, eaque ipsa quae ab illo inventore veritatis et quasi architecto</p>
</div>
<div class="band-dots"><span></span><span></span></div>

<h2 class="team-title">Our Team</h2>
<div class="team-arrow" style="left:154px"><svg width="12" height="12" viewBox="0 0 12 12"><path d="M8 2L4 6l4 4" fill="none" stroke="#fff" stroke-width="2"/></svg></div>
<div class="team-arrow" style="left:1008px"><svg width="12" height="12" viewBox="0 0 12 12"><path d="M4 2l4 4-4 4" fill="none" stroke="#fff" stroke-width="2"/></svg></div>
<div class="member" style="left:234px"><div class="member-photo" role="img" aria-label="Portrait photo of team member Joseva"></div><div class="member-name">Joseva</div></div>
<div class="member" style="left:424px"><div class="member-photo" role="img" aria-label="Portrait photo of team member Amera"></div><div class="member-name">Amera</div></div>
<div class="member" style="left:614px"><div class="member-photo" role="img" aria-label="Portrait photo of team member Smith"></div><div class="member-name">Smith</div></div>
<div class="member" style="left:804px"><div class="member-photo" role="img" aria-label="Portrait photo of team member John"></div><div class="member-name">John</div></div>

<section class="newsletter">
  <h2>Newsletter Subscribe</h2>
  <p>Placerat vehicula id suspendisse lorem eget. Vel et gravida. Non a dapibus eget scelerisque quisque curabitur leo wisi pulvinar erat morbi.</p>
  <div class="email-field">Enter Email id</div>
  <div class="subscribe-btn">SUBSCRIBE</div>
</section>

<footer class="site-footer">
  <div class="footer-brand">Tarnby</div>
  <p class="footer-about">Morbi et orci. Nulla quam a. Diam sapien eu a nisi dignissim. Vestibulum et sit arcu</p>
  <div class="read-more">Read more</div>

  <h3 class="footer-head" style="left:390px">Quick Links</h3>
  <div class="quick-links"><span>Home</span><span>Our Team</span><span>About</span><span>Testimonials</span><span>Services</span><span>Contact Us</span></div>

  <h3 class="footer-head" style="left:629px">Contact Us</h3>
  <div class="contact-row" style="top:100px"><div class="contact-icon"><svg width="12" height="16" viewBox="0 0 12 16"><path d="M6 0a6 6 0 0 1 6 6c0 4-6 10-6 10S0 10 0 6a6 6 0 0 1 6-6z" fill="#2a78c2"/><circle cx="6" cy="6" r="2" fill="#1b202b"/></svg></div><span>#123, Lorium ipsum,Dolor<br>Amit. Newzland.</span></div>
  <div class="contact-row" style="top:152px"><div class="contact-icon"><svg width="14" height="10" viewBox="0 0 14 10"><rect width="14" height="10" fill="#2a78c2"/><path d="M0 0l7 5 7-5" fill="none" stroke="#1b202b" stroke-width="1.2"/></svg></div><span>hello@tarnby.com.au</span></div>
  <div class="contact-row" style="top:198px"><div class="contact-icon"><svg width="14" height="14" viewBox="0 0 14 14"><path d="M3 0l3 3-2 2c1 2 3 4 5 5l2-2 3 3-2 3C6 14 0 8 0 3z" fill="#2a78c2"/></svg></div><span>1-800 555 0142</span></div>

  <h3 class="footer-head" style="left:917px">Follow Us</h3>
  <div class="social"><span></span><span></span><span></span><span></span></div>
  <p class="footer-legal">© 2018. Company Name<br>All Right Reserved</p>
</footer>

</body>
</html>
```